FRESH WEB DESIGN FOR A HEALTH - SOCIAL NETWORK

We are currently looking for a creative, fresh, vibrant, inspiring design for a new social network focused on health and nutrition for health professionals (namely nutritionists) and end-users.

Design requirements - IMPORTANT: please see attached file 'LumaCrest web site design scope' for the detailed brief.

The web site requires new design templates with inter-changeable banners and in some cases profile images. It's important for the website to communicate LumaCrest's core values and image which includes fun, vitality, freshness, life fulfillment, trust, integrity and loyalty to the two target groups. Imagery must have a consistent/inter-related theme across all communities, topics and resources, which need to be easily applied to the web site.To help engage our audience we are looking for something fresh and unique in the selected imagery/ theme/ design templates.

The chosen design will need to be applied to create a PDF, PowerPoint and business card template.

Please see attached file 'LumaCrest web site design scope' to view the LumaCrest web site, which is currently under development.

Nutrition

```html
<!DOCTYPE html>
<html lang="en">
<head>
<meta charset="utf-8">
<title>LumaCrest – Health Social Network</title>
<link rel="stylesheet" href="https://fonts.googleapis.com/css2?family=Open+Sans:ital,wght@0,300;0,400;0,600;0,700;1,700&family=Roboto+Condensed:wght@300;700&family=PT+Serif&display=swap">
<style>
:root{
  --blue:#1b8fd2;
  --blue-dark:#1474b3;
  --blue-light:#4cb5e8;
  --navy:#24304a;
  --green:#8cc63f;
  --yellow:#d8d53a;
  --gray-bg:#efefef;
  --footer:#4a4a4c;
  --text:#333;
  --white:#fff;
}
*{margin:0;padding:0;box-sizing:border-box}
html,body{width:1200px;height:3000px;overflow:hidden}
body{position:relative;background:var(--white);font-family:"Open Sans",sans-serif;color:var(--text)}
.abs{position:absolute}
.serif{font-family:"PT Serif",serif}

/* header */
.header{left:0;top:0;width:1200px;height:150px;background:var(--white)}
.brand{left:60px;top:50px;display:flex;align-items:center;gap:14px}
.brand-dot{width:34px;height:34px;border-radius:50%;background:var(--green)}
.brand-name{font-size:40px;font-weight:700;color:var(--blue);letter-spacing:-1px}
.nav{left:372px;top:60px;display:flex;gap:36px;font-size:19px;color:#444}
.showcases{left:910px;top:62px;font-size:19px;color:#444}
.btn-appoint{left:1035px;top:50px;width:140px;height:50px;background:var(--blue-light);color:var(--white);font-size:14px;font-weight:700;display:flex;align-items:center;justify-content:center;border-radius:3px}

/* hero */
.hero{left:0;top:150px;width:1200px;height:535px;background:linear-gradient(135deg,#bfe3f7 0%,#49b0e6 45%,#2f9fdc 100%)}
.hero-photo{left:700px;top:150px;width:500px;height:535px;background:linear-gradient(180deg,#d8eef9,#a9d8f1 60%,#7fc4ea)}
.hero-title{left:120px;top:312px;font-size:50px;line-height:60px;font-weight:300;color:var(--white);letter-spacing:.5px}
.hero-sub{left:122px;top:382px;width:420px;font-size:19px;line-height:27px;color:var(--white)}
.btn-show{left:125px;top:470px;width:310px;height:64px;background:var(--blue-dark);color:var(--white);font-size:22px;display:flex;align-items:center;justify-content:center;border-radius:4px;letter-spacing:1px}
.slider-dot{left:16px;width:12px;height:12px;border-radius:50%}

/* about */
.care-photo{left:120px;top:605px;width:330px;height:215px;background:linear-gradient(135deg,#e9f3f7,#b9d5e0);border:8px solid var(--white);box-shadow:0 3px 10px rgba(0,0,0,.35)}
.care-title{left:140px;top:838px;font-family:"Roboto Condensed",sans-serif;font-weight:700;font-size:46px;line-height:44px;color:#111}
.care-title .light{font-weight:300}
.care-note{left:142px;top:922px;font-size:14px;font-weight:700;font-style:italic;color:var(--green)}
.about-label{left:553px;top:750px;width:205px;height:26px;background:var(--green);color:var(--white);font-weight:700;font-style:italic;font-size:16px;padding-left:8px;line-height:26px}
.about-text{left:553px;top:782px;width:617px;font-size:15.5px;line-height:21px;color:#222}
.about-more{left:553px;top:892px;font-size:15px;font-weight:700;font-style:italic;color:#111}

/* talk */
.talk-bg{left:0;top:1000px;width:1200px;height:495px;background:var(--gray-bg)}
.section-title{left:0;width:1200px;text-align:center;font-size:58px;font-weight:400;color:var(--navy)}
.section-text{left:220px;width:760px;text-align:center;font-size:14px;line-height:17px;color:#444}
.feature{top:1225px;width:220px;text-align:center}
.feature svg{display:block;margin:0 auto}
.feature-name{font-size:22px;color:var(--navy);margin-top:12px}
.feature-name .amp{color:var(--blue)}
.feature-text{font-size:13px;line-height:16px;color:#444;margin-top:6px}

/* bands */
.band{left:0;width:1200px;height:225px;background:var(--blue);text-align:center;color:var(--white)}
.band-photo{background:linear-gradient(180deg,#a7dcf4,#7ccbef 50%,#a8daf1)}
.band-kicker{margin-top:45px;font-size:18px;letter-spacing:5px}
.band-title{font-size:50px;font-weight:300;margin-top:2px;letter-spacing:.5px}
.band-btn{display:inline-block;margin-top:8px;padding:6px 18px;background:var(--white);color:var(--blue);font-size:22px;letter-spacing:1px;border:2px solid var(--blue-light)}

/* cards */
.card{top:1960px;width:295px}
.card-photo{width:295px;height:205px;background:linear-gradient(135deg,#eef4f7,#bcd3de)}
.card-title{font-size:23px;font-weight:400;color:#222;margin-top:36px}
.card-text{font-size:15px;line-height:18px;color:#333;margin-top:4px}
.card-btn{width:140px;height:40px;background:var(--blue-light);color:var(--white);font-size:12px;font-weight:700;display:flex;align-items:center;justify-content:center;border-radius:3px;margin-top:18px}

/* footer */
.footer{left:0;top:2610px;width:1200px;height:390px;background:var(--footer)}
.footer-box{left:120px;top:2610px;width:265px;height:370px;background:#2da4e0;padding:26px 18px}
.footer-brand{font-size:30px;font-weight:700;color:#111;letter-spacing:-1px}
.footer-about{font-size:12.5px;line-height:16px;font-weight:700;color:#111;margin-top:12px}
.footer-col{top:2655px;width:190px}
.footer-col h3{font-size:28px;font-weight:400;color:var(--white);margin-bottom:14px}
.footer-col li{list-style:none;font-size:13px;color:#eee;height:40px;line-height:40px;border-bottom:1px solid #626264}
.copyright{left:400px;top:2942px;font-size:13px;color:#ddd;letter-spacing:1px}
.copyright b{color:var(--white)}
.pay{top:2938px;width:42px;height:26px;border-radius:3px}
</style>
</head>
<body>

<header class="abs header">
  <div class="abs brand"><span class="brand-dot"></span><span class="brand-name">LumaCrest</span></div>
  <nav class="abs nav"><span>Home</span><span>features</span><span>appointments</span><span>support</span></nav>
  <div class="abs showcases">showcases ▾</div>
  <div class="abs btn-appoint">APPOINTMENT</div>
</header>

<section>
  <div class="abs hero"></div>
  <div class="abs hero-photo" role="img" aria-label="Smiling doctor in a white coat with a stethoscope"></div>
  <h1 class="abs hero-title">INCREDIBILE SERVICE</h1>
  <p class="abs hero-sub">LumaCrest provides everything you need to ensure you have the luxury you deserve.</p>
  <div class="abs btn-show">VISIT OUR SHOWROOM!</div>
  <span class="abs slider-dot" style="top:393px;background:var(--yellow)"></span>
  <span class="abs slider-dot" style="top:414px;background:var(--white)"></span>
  <span class="abs slider-dot" style="top:435px;background:var(--green)"></span>
</section>

<section>
  <div class="abs care-photo" role="img" aria-label="Doctor caring for an elderly patient"></div>
  <h2 class="abs care-title">ALL THE CARE<br>THAT <span class="light">YOU NEED</span></h2>
  <p class="abs care-note">at lumacrest we provide it for you</p>
  <div class="abs about-label">ABOUT LUMACREST</div>
  <p class="abs about-text">LumaCrest shows people how they can have more energy and time in their life by simply having the right nutrition, having the right mind-set and exercising. LumaCrest's social network health forum educates people on how they can present and overcome disease by leading a healthy, natural and mindful life.</p>
  <p class="abs about-more">CLICK TO SEE MORE</p>
</section>

<section>
  <div class="abs talk-bg"></div>
  <h2 class="abs section-title" style="top:1035px">LET’S TALK ABOUT US</h2>
  <p class="abs section-text serif" style="top:1112px">Lorem ipsum dolor sit amet, consectetuer adipiscing elit, sed diam nonummy nibh euismod tincidunt ut laoreet dolore magna aliquam erat volutpat. Ut wisi enim ad minim veniam, quis nostrud exerci tation ullamcorper ut vero eros et accumsan.</p>

  <div class="abs feature" style="left:115px">
    <svg width="96" height="96" viewBox="0 0 96 96"><circle cx="48" cy="48" r="46" fill="var(--blue)"/><path d="M48 68 L30 50 a11 11 0 0 1 18-14 a11 11 0 0 1 18 14 Z" fill="none" stroke="#fff" stroke-width="4" stroke-linejoin="round"/></svg>
    <div class="feature-name">Nutrition</div>
    <p class="feature-text serif">Lorem ipsum dolor sit amet, consectetuer adipiscing elit, sed diam nonummy nibh euismod tincidunt ut laoreet dolore magna.</p>
  </div>
  <div class="abs feature" style="left:370px">
    <svg width="96" height="96" viewBox="0 0 96 96"><circle cx="48" cy="48" r="46" fill="var(--blue)"/><path d="M48 26 V70 M26 48 H70" stroke="#fff" stroke-width="5" stroke-linecap="round"/></svg>
    <div class="feature-name">Energy <span class="amp">&amp;</span> Mind</div>
    <p class="feature-text serif">Lorem ipsum dolor sit amet, consectetuer adipiscing elit, sed diam nonummy nibh euismod tincidunt ut laoreet dolore magna.</p>
  </div>
  <div class="abs feature" style="left:625px">
    <svg width="96" height="96" viewBox="0 0 96 96"><circle cx="48" cy="48" r="46" fill="var(--blue)"/><path d="M48 24 L68 32 V48 C68 60 58 68 48 72 C38 68 28 60 28 48 V32 Z" fill="none" stroke="#fff" stroke-width="4" stroke-linejoin="round"/><path d="M39 48 L46 55 L58 42" fill="none" stroke="#fff" stroke-width="4" stroke-linecap="round" stroke-linejoin="round"/></svg>
    <div class="feature-name">Wellness</div>
    <p class="feature-text serif">Lorem ipsum dolor sit amet, consectetuer adipiscing elit, sed diam nonummy nibh euismod tincidunt ut laoreet dolore magna.</p>
  </div>
  <div class="abs feature" style="left:865px">
    <svg width="96" height="96" viewBox="0 0 96 96"><circle cx="48" cy="48" r="46" fill="var(--blue)"/><circle cx="48" cy="52" r="18" fill="none" stroke="#fff" stroke-width="4"/><path d="M48 52 V41 M44 28 H52 M48 28 V34" stroke="#fff" stroke-width="4" stroke-linecap="round"/></svg>
    <div class="feature-name">Exercise</div>
    <p class="feature-text serif">Lorem ipsum dolor sit amet, consectetuer adipiscing elit, sed diam nonummy nibh euismod tincidunt ut laoreet dolore magna.</p>
  </div>
</section>

<section class="abs band" style="top:1495px">
  <p class="band-kicker">HEALTH AND NUTRITIONAL ADVICE</p>
  <h2 class="band-title">CONSULTATIONS AND GROUP WORKSHOPS</h2>
  <span class="band-btn">VISIT OUR SHOWROOM!</span>
</section>

<section>
  <h2 class="abs section-title" style="top:1755px">LET’S TALK ABOUT US</h2>
  <p class="abs section-text serif" style="top:1835px">Lorem ipsum dolor sit amet, consectetuer adipiscing elit, sed diam nonummy nibh euismod tincidunt ut laoreet dolore magna aliquam erat volutpat. Ut wisi enim ad minim veniam, quis nostrud exerci tation ullamcorper ut vero eros et accumsan.</p>

  <article class="abs card" style="left:122px">
    <div class="card-photo" role="img" aria-label="Doctor visiting a child in a hospital bed"></div>
    <h3 class="card-title">Maintaining Health</h3>
    <p class="card-text serif">Lorem ipsum dolor sit amet, consectetuer adipiscing elit, sed diam nonummy nibh euismod tincidunt ut laoreet dolore magna.</p>
    <div class="card-btn">APPOINTMENT</div>
  </article>
  <article class="abs card" style="left:457px">
    <div class="card-photo" role="img" aria-label="Doctor examining a young girl"></div>
    <h3 class="card-title">Maintaining Health</h3>
    <p class="card-text serif">Lorem ipsum dolor sit amet, consectetuer adipiscing elit, sed diam nonummy nibh euismod tincidunt ut laoreet dolore magna.</p>
    <div class="card-btn">APPOINTMENT</div>
  </article>
  <article class="abs card" style="left:790px">
    <div class="card-photo" role="img" aria-label="Doctor consulting a patient at a desk"></div>
    <h3 class="card-title">Maintaining Health</h3>
    <p class="card-text serif">Lorem ipsum dolor sit amet, consectetuer adipiscing elit, sed diam nonummy nibh euismod tincidunt ut laoreet dolore magna.</p>
    <div class="card-btn">APPOINTMENT</div>
  </article>
</section>

<section class="abs band band-photo" style="top:2385px" role="img" aria-label="Light blue tinted photo of a clinic consultation">
  <p class="band-kicker">HEALTH AND NUTRITIONAL ADVICE</p>
  <h2 class="band-title">CONSULTATIONS AND GROUP WORKSHOPS</h2>
  <span class="band-btn">VISIT OUR SHOWROOM!</span>
</section>

<footer>
  <div class="abs footer"></div>
  <div class="abs footer-box">
    <div class="footer-brand">LumaCrest</div>
    <p class="footer-about">Lorem ipsum dolor sit amet, consectetuer adipiscing elit, sed diam nonummy nibh euismod tincidunt ut laoreet dolore magna aliquam erat volutpat. Ut wisi enim ad minim veniam, quis nostrud exerci tation ullamcorper suscipit lobortis nisl ut aliquip ex ea commodo consequat. Duis autem vel eum iriure dolor in hendrerit in vulputate velit esse molestie consequat, vel illum dolore eu feugiat nulla facilisis at vero eros et accumsan.</p>
  </div>
  <div class="abs footer-col" style="left:465px">
    <h3>ABOUT</h3>
    <ul><li>About SilverRide</li><li>Terms &amp; Conditions</li><li>Privacy Policy</li><li>Track Your Order</li><li>Disclaimer</li></ul>
  </div>
  <div class="abs footer-col" style="left:690px">
    <h3>NEW CARS</h3>
    <ul><li>New Collection</li><li>Panthera (2015)</li><li>Limo Collection</li><li>Exclusive Offers</li><li>Sale</li></ul>
  </div>
  <div class="abs footer-col" style="left:920px">
    <h3>FOLLOW US</h3>
    <ul><li>Friendwall</li><li>Chirpline</li><li>Snapframe</li><li>Reelhub</li><li>Pinboardly</li></ul>
  </div>
  <p class="abs copyright">© <b>LUMACREST</b> 2012-2015 ALL RIGHTS RESERVED</p>
  <span class="abs pay" style="left:870px;background:#6e8fb8"></span>
  <span class="abs pay" style="left:922px;background:#d9d9d9"></span>
  <span class="abs pay" style="left:974px;background:#2c76c5"></span>
  <span class="abs pay" style="left:1026px;background:#1f4f9e"></span>
</footer>

</body>
</html>
```